Keystone Leadership Transformation Roadmap

I've included a mock up of what I like. This design needs to be made better. I like the top section layout. It needs 5 circles for:

Please create a webpage based on this design, but improve it. Use the letterhead and business card brand you created for me to make the brand look seamless.

I love the circles - please make 5 of them the same size (can be 1 lines)

Here is the text for the circles:

Headline: Your Guided Path to Transformation
Text
Step 1: The Initial Consultation
text
Step 2: Deep-Dive Discovery and Assessment
text
Step 3: Synthesis and Strategy Formulation
text
Step 4: The Strategic Debrief Session
Text
Step 5: Implementation and Ongoing Support
Text

Also, there are many sections to this page including:

Introduction
Copy
Copy
Bio
CTA
FAQ's

Please make it interesting.

Use the colors of the mockup and my website: Corinna Halvard.com
I am including my letterhead and business card for brand coherence.

Use the fonts on my website. CorinnaHalvard.com

I will need all files to send to the developer. We must have ALL the art files.

Target Market(s)

see my website; CorinnaHalvard.com

Industry/Entity Type

See my uploads

Requirements
Must have
• all the design files

```html
<!DOCTYPE html>
<html lang="en">
<head>
<meta charset="utf-8">
<title>Keystone Leadership Transformation</title>
<link rel="stylesheet" href="https://fonts.googleapis.com/css2?family=Archivo:wght@400;500&family=Cormorant+Garamond:wght@500;600;700&family=Open+Sans:wght@400;600;700&display=swap">
<style>
:root{
  --navy:#1b2a33;
  --navy-deep:#16232b;
  --teal:#2d7388;
  --teal-line:#3e8aa0;
  --gold:#c9a14a;
  --gold-light:#e6c373;
  --gold-dark:#9c6f2c;
  --brown:#74512c;
  --ink:#2a2f33;
  --ice:#e7f2f9;
  --cream:#f7efe3;
  --white:#ffffff;
}
*{margin:0;padding:0;box-sizing:border-box}
html,body{width:1200px;height:5213px;overflow:hidden}
body{position:relative;background:var(--white);font-family:"Open Sans",Arial,sans-serif;color:var(--ink)}
.abs{position:absolute}
.display{font-family:"Archivo",Arial,sans-serif;font-weight:400;text-transform:uppercase;letter-spacing:.5px;color:var(--navy)}
.btn{position:absolute;display:flex;align-items:center;justify-content:center;border-radius:24px;font-family:"Archivo",Arial,sans-serif;font-size:15px;color:var(--navy);text-transform:uppercase;background:linear-gradient(180deg,#b88a45,#8c6434);box-shadow:0 3px 8px rgba(0,0,0,.25)}
.btn.shine{background:linear-gradient(90deg,#8a5f2c,#e2bd6a 50%,#8a5f2c)}
.center{left:0;width:1200px;text-align:center}
.kicker{position:absolute;left:0;width:1200px;display:flex;justify-content:center;align-items:center;gap:14px;font-family:"Cormorant Garamond",Georgia,serif;font-weight:600;font-size:17px;letter-spacing:1px;color:var(--teal);text-transform:uppercase}
.kicker::before,.kicker::after{content:"";width:28px;height:2px;background:var(--teal)}
.kicker.light{color:#fff}.kicker.light::before,.kicker.light::after{background:#fff}
.emblem{position:absolute;width:70px;height:70px;border-radius:50%;border:3px solid var(--gold);background:#e4f0f5}
.emblem.on-teal{border-color:#fff;background:#cfe5ec}

/* brand wordmark */
.brand{position:absolute;display:flex;flex-direction:column;align-items:center;text-align:center}
.brand .dot{border-radius:50%;border:3px solid var(--gold);margin-bottom:10px}
.brand .name{font-family:"Archivo",Arial,sans-serif;font-weight:400;color:#fff;text-transform:uppercase;letter-spacing:1px}
.brand.top{left:108px;top:16px;width:190px}
.brand.top .dot{width:84px;height:84px}
.brand.top .name{font-size:15px;line-height:20px}
.brand.foot{left:111px;top:90px;width:268px}
.brand.foot .dot{width:120px;height:120px}
.brand.foot .name{font-size:22px;line-height:30px}

/* header */
.hero{position:absolute;left:0;top:0;width:1200px;height:860px;background:var(--navy)}
.hero::before{content:"";position:absolute;left:0;top:0;width:1200px;height:3px;background:var(--gold)}
.nav a{position:absolute;top:68px;font-family:"Archivo",Arial,sans-serif;font-size:15px;color:#fff;text-decoration:none}
.nav a.active{color:var(--gold-light)}
.hero h1{position:absolute;left:109px;top:238px;font-family:"Archivo",Arial,sans-serif;font-weight:400;font-size:45px;line-height:56px;color:#fff;text-transform:uppercase}
.hero h1 span{color:var(--gold-light)}
.hero .lede{position:absolute;left:110px;top:418px;width:420px;font-size:16px;line-height:26px;color:#fff}
.portrait{position:absolute;left:610px;top:105px;width:440px;height:520px;border-radius:220px 220px 0 0;background:radial-gradient(ellipse at 50% 35%,#c98f6e 0 22%,#6a3b2a 38%,#20332f 70%,var(--navy) 100%)}

/* benefit circles */
.benefit{position:absolute;border-radius:50%;background:#fff;border:4px solid var(--gold);box-shadow:0 6px 16px rgba(0,0,0,.18);display:flex;flex-direction:column;align-items:center;justify-content:center;text-align:center;padding:0 30px}
.benefit .ico{width:24px;height:24px;border-radius:50%;border:3px solid var(--gold);margin-bottom:7px;flex:none}
.benefit h3{font-family:"Cormorant Garamond",Georgia,serif;font-weight:600;font-size:18px;line-height:21px;color:var(--ink);margin-bottom:6px}
.benefit p{font-size:11.5px;line-height:17px;color:var(--ink)}
.benefit.feature{background:radial-gradient(circle at 40% 30%,#e7c77e,#b5843d 70%,#966a2e);border-color:#f0d9a0;padding:0 32px}
.benefit.feature .ico{border-color:var(--navy);border-radius:4px}
.benefit.feature h3{font-size:20px}
.benefit.feature p{font-size:10.5px;line-height:17px}

.intro{position:absolute;top:916px;font-size:15.5px;line-height:31px;color:var(--ink)}

/* steps */
.step{position:absolute;width:228px;height:228px;border-radius:50%;background:linear-gradient(135deg,#6e4a26,#b8873e 45%,#e4c274 60%,#7b5530);box-shadow:0 8px 18px rgba(0,0,0,.25)}
.step .inner{position:absolute;left:22px;top:22px;width:184px;height:184px;border-radius:50%;background:#fff;display:flex;flex-direction:column;align-items:center;justify-content:center;text-align:center;padding:0 14px}
.step .inner .ico{width:44px;height:40px;border-radius:8px;background:linear-gradient(180deg,#d5ad5c,#8c6434);margin-bottom:12px}
.step h4{font-family:"Cormorant Garamond",Georgia,serif;font-weight:700;font-size:15px;line-height:21px;color:var(--navy);text-transform:uppercase}
.step .num{position:absolute;left:96px;top:-14px;width:36px;height:36px;border-radius:50%;background:linear-gradient(180deg,#d8b062,#9a6d2f);border:2px solid #fff;color:#fff;font-family:"Archivo",Arial,sans-serif;font-size:15px;display:flex;align-items:center;justify-content:center}

/* about */
.about-band{position:absolute;left:0;top:1720px;width:1200px;height:640px;background:linear-gradient(180deg,#fff,var(--cream))}
.about-halo{position:absolute;left:0;top:1770px;width:560px;height:560px;border-radius:50%;background:radial-gradient(circle,rgba(212,185,140,0) 0 44%,rgba(212,185,140,.35) 46%,rgba(180,205,215,.25) 60%,rgba(255,255,255,0) 72%)}
.about-photo{position:absolute;left:50px;top:1811px;width:466px;height:466px;border-radius:50%;background:radial-gradient(ellipse at 50% 40%,#c99478 0 20%,#5b3524 36%,#1f3c4c 62%,#16303d)}
.about-copy{position:absolute;left:590px;width:510px;text-align:center;font-size:14.5px;line-height:27.5px;color:var(--ink)}

/* teal */
.teal-copy{position:absolute;left:160px;width:880px;text-align:center;color:#fff;font-size:17.5px;line-height:31px}

/* sectors */
.sector{position:absolute;top:3572px;height:254px;background:#fff;border-radius:8px;box-shadow:0 4px 14px rgba(0,0,0,.18);padding:10px}
.sector .pic{height:170px;border-radius:4px}
.sector .label{margin-top:10px;text-align:center;font-family:"Cormorant Garamond",Georgia,serif;font-weight:600;font-size:16px;line-height:26px;color:var(--ink);text-transform:uppercase}

/* faq */
.faq-band{position:absolute;left:0;top:4018px;width:1200px;height:840px;background:var(--ice)}
.faq{position:absolute;left:111px;width:978px;height:56px;background:#fff;border-radius:28px;box-shadow:0 2px 8px rgba(20,60,80,.08);display:flex;align-items:center;justify-content:space-between;padding:0 30px;font-size:15px;color:var(--ink)}
.faq .plus{width:18px;height:18px;border-radius:50%;background:#8c8f92;position:relative}
.faq .plus::before,.faq .plus::after{content:"";position:absolute;background:#fff;left:4px;top:8px;width:10px;height:2px}
.faq .plus::after{transform:rotate(90deg)}

/* footer */
.footer{position:absolute;left:0;top:4860px;width:1200px;height:353px;background:var(--navy-deep)}
.foot-text{position:absolute;font-size:14px;line-height:30px;color:#fff}
</style>
</head>
<body>

<!-- HERO -->
<section class="hero">
  <div class="brand top">
    <div class="dot"></div>
    <div class="name">Keystone Leadership Transformation</div>
  </div>
  <nav class="nav">
    <a class="active" style="left:362px">Home</a>
    <a style="left:455px">Coaching</a>
    <a style="left:567px">Retreats</a>
    <a style="left:676px">About</a>
    <a style="left:763px">Insights</a>
    <a style="left:864px">Contact</a>
  </nav>
  <div class="btn" style="left:980px;top:59px;width:108px;height:38px;font-size:14px;text-transform:none;background:linear-gradient(180deg,#d4ac5c,#a9803d)">Get A Quote</div>
  <div class="portrait" role="img" aria-label="Portrait photograph of the coach, smiling, dark blazer"></div>
  <h1>Support your<br>leadership efforts<br>with <span>elite coaching</span></h1>
  <p class="lede">Introducing Keystone Leadership Coaching and Organization Development</p>
  <div class="btn" style="left:111px;top:489px;width:245px;height:44px">Book a discovery call</div>
</section>

<svg class="abs" style="left:0;top:640px" width="1200" height="260" viewBox="0 0 1200 260">
  <path d="M0 0H1200V120C950 110 700 130 420 170C250 195 110 200 0 180Z" fill="#1b2a33"/>
  <path d="M0 190C200 200 420 170 640 140C860 112 1040 108 1200 112" fill="none" stroke="#c9a14a" stroke-width="6"/>
  <path d="M0 205C220 215 460 185 680 158C880 133 1060 126 1200 128" fill="none" stroke="#2d7388" stroke-width="4"/>
</svg>

<div class="benefit" style="left:139px;top:607px;width:232px;height:232px">
  <div class="ico"></div>
  <h3>Exclusivity and<br>Tailored Strategies</h3>
  <p>This is not a one-size-fits-all program.</p>
</div>
<div class="benefit" style="left:356px;top:597px;width:232px;height:232px">
  <div class="ico" style="border-radius:4px"></div>
  <h3>Strategic<br>Decision-Making</h3>
  <p>As a leader, you face complex decisions with far-reaching consequences.</p>
</div>
<div class="benefit" style="left:829px;top:594px;width:232px;height:232px">
  <div class="ico" style="border-radius:4px"></div>
  <h3>Navigating<br>Organizational Challenges</h3>
  <p>Keystone coaching provides expert guidance &amp; an objective perspective to help you navigate these complexities.</p>
</div>
<div class="benefit feature" style="left:560px;top:580px;width:280px;height:280px">
  <div class="ico"></div>
  <h3>Leadership Development</h3>
  <p>Even the most accomplished leaders have room to grow. This coaching focuses on refining your unique leadership capabilities, whether that means enhancing your executive presence, inspiring high-performing teams, or leading transformative change.</p>
</div>

<p class="intro center">Elite coaching provides a confidential, strategic partnership designed to elevate the performance of top executives<br>and their organizations. This bespoke service focuses on the specific, high-stakes challenges that leaders face.<br>Below is an expansion of the core benefits you can expect from this exclusive engagement.</p>

<!-- STEPS -->
<div class="emblem" style="left:565px;top:1079px"></div>
<h2 class="display center abs" style="top:1158px;font-size:44px;line-height:53px">Your guided path to<br>transformation</h2>
<div class="kicker" style="top:1267px">Five steps</div>
<p class="center abs" style="top:1313px;font-size:15.5px;line-height:30px">Duis aute irure dolor in reprehenderit in voluptate velit esse cillum dolore eu fugiat nulla pariatur. Excepteur<br>sint occaecat qui officia deserunt mollit anim id est laborum.</p>

<div class="step" style="left:83px;top:1408px"><div class="num">01</div><div class="inner"><div class="ico" role="img" aria-label="Consultation icon"></div><h4>The initial<br>consultation</h4></div></div>
<div class="step" style="left:286px;top:1408px"><div class="num">02</div><div class="inner"><div class="ico" role="img" aria-label="Assessment checklist icon"></div><h4>Deep-dive<br>discovery and<br>assessment</h4></div></div>
<div class="step" style="left:488px;top:1408px"><div class="num">03</div><div class="inner"><div class="ico" role="img" aria-label="Strategy icon"></div><h4>Synthesis and<br>strategy<br>formulation</h4></div></div>
<div class="step" style="left:691px;top:1408px"><div class="num">04</div><div class="inner"><div class="ico" role="img" aria-label="Debrief meeting icon"></div><h4>The strategic<br>debrief session</h4></div></div>
<div class="step" style="left:890px;top:1408px"><div class="num">05</div><div class="inner"><div class="ico" role="img" aria-label="Support icon"></div><h4>Implementation<br>and ongoing<br>support</h4></div></div>

<!-- ABOUT -->
<div class="about-band"></div>
<div class="about-halo" role="img" aria-label="Faint decorative ring behind the portrait"></div>
<div class="about-photo" role="img" aria-label="Portrait photograph of Corinna Halvard"></div>
<div class="emblem" style="left:806px;top:1745px"></div>
<h2 class="display abs" style="left:580px;width:530px;text-align:center;top:1826px;font-size:44px">Corinna Halvard</h2>
<div class="kicker" style="left:580px;width:530px;top:1882px">About me</div>
<p class="about-copy" style="top:1916px">As a top leader, you deserve an elite partnership designed exclusively for you—especially when you need a woman you can count on. With a perspective rooted in both wisdom and empathy, I offer insights, intuition, and support that many male coaches simply cannot replicate.</p>
<p class="about-copy" style="top:2054px">My mission is to guide high-performing leaders and their teams toward a state of peak performance defined by stress-free resilience, heightened productivity, and effortless flow. I founded Corinna Halvard International to provide effective, accelerated training that unlocks the highest levels of human potential.</p>
<div class="btn" style="left:722px;top:2215px;width:246px;height:43px">Book a discovery call</div>

<!-- TEAL -->
<svg class="abs" style="left:0;top:2330px" width="1200" height="960" viewBox="0 0 1200 960">
  <path d="M0 90C300 110 700 110 1000 60C1100 45 1160 30 1200 20V900C900 860 500 855 180 880C100 887 40 897 0 905Z" fill="#2d7388"/>
  <path d="M0 70C320 95 720 90 1010 45C1110 30 1170 15 1200 5" fill="none" stroke="#1b2a33" stroke-width="10"/>
  <path d="M1200 12C1160 25 1100 40 1010 55" fill="none" stroke="#c9a14a" stroke-width="6"/>
  <path d="M0 930C160 880 420 860 640 860" fill="none" stroke="#c9a14a" stroke-width="6"/>
  <path d="M0 918C200 880 460 865 700 868" fill="none" stroke="#3e8aa0" stroke-width="4"/>
</svg>
<div class="emblem on-teal" style="left:565px;top:2542px"></div>
<h2 class="display center abs" style="top:2622px;font-size:44px;line-height:51px;color:#fff">Keystone leadership is the secret to<br>lasting organization success...</h2>
<div class="kicker light" style="top:2733px">Success</div>
<p class="teal-copy" style="top:2771px">Experience transformative results with a bespoke roadmap, dedicated one-on-one guidance, and confidential, high-impact strategies tailored to your unique vision. Take your organization to new heights—unlock the full potential of your leadership with exclusive Keystone Leadership Coaching and Organization Development Consulting.</p>
<p class="teal-copy" style="top:2926px;font-weight:700">Your Leadership Transformation Awaits.</p>
<p class="teal-copy" style="top:2957px;left:130px;width:940px">Step into a partnership designed exclusively for leaders like you—visionary, driven, and ready to redefine success. With tailored strategies, expert guidance, and a commitment to unlocking your highest potential, the next chapter of your leadership journey starts here.</p>
<div class="btn" style="left:478px;top:3078px;width:245px;height:43px">Book a discovery call</div>

<!-- SECTORS -->
<div class="emblem" style="left:565px;top:3316px"></div>
<h2 class="display center abs" style="top:3396px;font-size:44px;line-height:51px">Empowering leaders<br>across a wide range of sectors</h2>
<div class="kicker" style="top:3504px">Sectors</div>

<div class="sector" style="left:-10px;width:202px"><div class="pic" role="img" aria-label="Photo of a professional with digital technology overlay" style="background:linear-gradient(135deg,#2c4a6e,#8aa6c4)"></div><div class="label">Technology<br>&amp; MSP's</div></div>
<div class="sector" style="left:225px;width:210px"><div class="pic" role="img" aria-label="Photo of a diverse team joining hands" style="background:linear-gradient(135deg,#3f6b3a,#c7a46a)"></div><div class="label">Universities &amp;<br>non- profits</div></div>
<div class="sector" style="left:478px;width:210px"><div class="pic" role="img" aria-label="Photo of hands on a laptop with legal and finance icons" style="background:linear-gradient(135deg,#16365a,#4d86b8)"></div><div class="label">Legal<br>&amp; finance</div></div>
<div class="sector" style="left:731px;width:216px"><div class="pic" role="img" aria-label="Photo of travellers watching a sunset by the sea" style="background:linear-gradient(180deg,#d88a3a,#5a4a5a)"></div><div class="label">Travel<br>&amp; lifestyle</div></div>
<div class="sector" style="left:984px;width:224px"><div class="pic" role="img" aria-label="Photo of a boutique owner with clothing rack" style="background:linear-gradient(135deg,#e5d9c8,#b55a3a)"></div><div class="label">Retail<br>&amp; media</div></div>

<div class="btn shine" style="left:530px;top:3882px;width:140px;height:45px">View more</div>

<!-- FAQ -->
<div class="faq-band"></div>
<div class="emblem" style="left:565px;top:4074px"></div>
<h2 class="display center abs" style="top:4160px;font-size:44px">Frequently asked questions</h2>
<div class="kicker" style="top:4222px">FAQ</div>
<div class="faq" style="top:4277px">1) Who is Keystone Leadership for?<span class="plus"></span></div>
<div class="faq" style="top:4350px">2) How is Keystone Leadership different from coaching?<span class="plus"></span></div>
<div class="faq" style="top:4423px">3) What can I expect from the initial consultation?<span class="plus"></span></div>
<div class="faq" style="top:4494px">4) How long does the process take?<span class="plus"></span></div>
<div class="faq" style="top:4567px">5) Is this program available virtually? What industries do you specialize in?<span class="plus"></span></div>
<div class="btn shine" style="left:526px;top:4681px;width:146px;height:46px">View more</div>

<!-- FOOTER -->
<footer class="footer">
  <div class="brand foot">
    <div class="dot"></div>
    <div class="name">Keystone Leadership Transformation</div>
  </div>
  <p class="foot-text" style="left:480px;top:90px;width:640px">Keystone Leadership Transformation is a trade name owned by Corinna Halvard International and The Resonant Wellness Institute.</p>
  <p class="foot-text" style="left:480px;top:165px">2026 Retreat</p>
  <p class="foot-text" style="left:630px;top:165px">About</p>
  <p class="foot-text" style="left:728px;top:165px">Insights</p>
  <span class="abs" style="left:805px;top:173px;width:18px;height:18px;border-radius:50%;background:#fff"></span>
  <p class="foot-text" style="left:480px;top:210px">Terms &amp; Policies</p>
  <p class="foot-text" style="left:654px;top:210px">Membership Agreement</p>
  <p class="foot-text" style="left:885px;top:210px">Contact</p>
  <p class="foot-text" style="left:480px;top:255px">Copyrights@2025.Keystone Leadership .All rights reserved.</p>
</footer>
<svg class="abs" style="left:0;top:4780px" width="1200" height="120" viewBox="0 0 1200 120">
  <path d="M0 40C300 85 800 70 1200 20V82H0Z" fill="#16232b"/>
  <path d="M0 30C320 78 820 62 1200 10" fill="none" stroke="#c9a14a" stroke-width="6"/>
  <path d="M0 42C320 92 820 76 1200 24" fill="none" stroke="#2d7388" stroke-width="5"/>
</svg>

</body>
</html>
```